Computer Training in the Education sector - Letterhead

We need a new letter head to be designed for the company. We provide computer training fro the Education Sector, both primary and private tertiary providers. The colours will need to tie in with the website www.lanternpathlearning.co.nz.
The company name is Lantern Path Co with the tag line of Computer Training for Educators.
The footer will need to have the following detail...
0508 KEY MENTOR
027 813 459
www.lanternpathlearning.co.nz / lessons@lanternpathlearning.co.nz
Updates

Thanks for the designs so far.

Some have watermarks in the background. Please don't worry about using watermarks as I will not be using a watermark in in a final design.
Regards,
Morris

Thank you for all the designs and the effort. There was some great concepts that came through.

Cheers
Morris

Industry/Entity Type

Computer

```html
<!DOCTYPE html>
<html lang="en">
<head>
<meta charset="utf-8">
<title>Lantern Path Co – Letterhead</title>
<link href="https://fonts.googleapis.com/css2?family=Open+Sans:wght@400;600&display=swap" rel="stylesheet">
<style>
  :root {
    --backdrop: #ebebeb;
    --sheet: #e8f5fd;
    --sheet-glow: #f7fbfe;
    --brand-blue: #3f8fd2;
    --rule-blue: #4aa6dc;
    --accent-orange: #ef6c1f;
    --text-grey: #5a5f66;
    --grass-light: #9ccc6a;
    --grass-dark: #5e9a3a;
  }
  * { box-sizing: border-box; margin: 0; padding: 0; }
  html, body {
    width: 1200px; height: 795px; overflow: hidden;
    background: var(--backdrop);
    font-family: "Open Sans", Arial, sans-serif;
  }
  .canvas {
    width: 1200px; height: 795px;
    display: flex; align-items: center; justify-content: center;
  }
  .letterhead {
    position: relative;
    width: 530px; height: 750px;
    background:
      linear-gradient(120deg, transparent 30%, var(--sheet-glow) 45%, transparent 62%),
      var(--sheet);
    box-shadow: 0 6px 18px rgba(0,0,0,.12);
    overflow: hidden;
  }
  .brand {
    position: absolute; left: 44px; top: 48px;
    display: flex; flex-direction: column; gap: 8px;
  }
  .brand-name {
    display: flex; align-items: center; gap: 10px;
    font-size: 20px; font-weight: 600; color: var(--brand-blue);
  }
  .brand-dot {
    width: 34px; height: 34px; border-radius: 50%;
    background: var(--brand-blue);
  }
  .tagline { font-size: 9.5px; color: var(--brand-blue); letter-spacing: .2px; }
  .grass-band {
    position: absolute; left: 0; right: 0; bottom: 92px; height: 40px;
    background: linear-gradient(180deg, rgba(156,204,106,0) 0%, var(--grass-light) 45%, var(--grass-dark) 100%);
  }
  .footer-rule {
    position: absolute; left: 0; right: 0; bottom: 89px; height: 3px;
    background: var(--rule-blue);
  }
  .footer {
    position: absolute; left: 40px; right: 30px; bottom: 30px;
    display: flex; justify-content: space-between; align-items: flex-end;
    font-size: 10px; color: var(--text-grey);
  }
  .footer-column { display: flex; flex-direction: column; gap: 8px; }
  .freephone { color: var(--accent-orange); font-size: 11px; font-weight: 600; letter-spacing: .3px; }
  .contact-item { display: flex; align-items: center; gap: 6px; }
  .contact-icon { width: 15px; height: 15px; flex: none; }
</style>
</head>
<body>
<main class="canvas">
  <article class="letterhead">
    <header class="brand">
      <div class="brand-name"><span class="brand-dot"></span>Lantern Path Co</div>
      <p class="tagline">Computer Training for Educators</p>
    </header>

    <div class="grass-band" role="img" aria-label="Strip of green grass along the bottom of the page"></div>
    <div class="footer-rule"></div>

    <footer class="footer">
      <div class="footer-column">
        <span class="freephone">0508 KEY MENTOR</span>
        <span class="contact-item">
          <svg class="contact-icon" viewBox="0 0 16 16" aria-hidden="true">
            <circle cx="8" cy="8" r="8" fill="#ef6c1f"/>
            <path d="M5.6 4.2l1.3 1.4-.7 1c.5 1.1 1.3 1.9 2.3 2.4l1-.7 1.4 1.3-.9 1.2C7.6 10.6 5.3 8.3 4.4 5.1z" fill="#fff"/>
          </svg>
          027 813 459
        </span>
      </div>
      <span class="contact-item">
        <svg class="contact-icon" viewBox="0 0 16 16" aria-hidden="true">
          <circle cx="8" cy="8" r="8" fill="#ef6c1f"/>
          <circle cx="8" cy="8" r="4" fill="none" stroke="#fff" stroke-width="1"/>
          <path d="M4 8h8M8 4c-1.6 2.4-1.6 5.6 0 8M8 4c1.6 2.4 1.6 5.6 0 8" fill="none" stroke="#fff" stroke-width=".8"/>
        </svg>
        www.lanternpathlearning.co.nz
      </span>
      <span class="contact-item">
        <svg class="contact-icon" viewBox="0 0 16 16" aria-hidden="true">
          <circle cx="8" cy="8" r="8" fill="#ef6c1f"/>
          <rect x="4" y="5.2" width="8" height="5.6" fill="none" stroke="#fff" stroke-width="1"/>
          <path d="M4 5.4l4 3 4-3" fill="none" stroke="#fff" stroke-width="1"/>
        </svg>
        lessons@lanternpathlearning.co.nz
      </span>
    </footer>
  </article>
</main>
</body>
</html>
```